Refrigeration & Air Conditioning modern and appealing

We want to design a business card that is modern and appealing using existing logo supplied

Front card
Residential Commercial Diary
RTA : AU052731
Licence L287456

Back card
Warren Kostig
Director
0491 357 208
info@frostlinerefrigeration.com.au
www.frostlinerefrigeration.com.au
• Air Conditioning
• Cool Rooms & Refrigeration
• Installation
• Service & Repair
• Preventative Maintenance

We offer 24/7 emergency service

```html
<!DOCTYPE html>
<html lang="en">
<head>
<meta charset="utf-8">
<title>Frostline Refrigeration &amp; Air Conditioning — Business Card</title>
<link href="https://fonts.googleapis.com/css2?family=Lato:wght@400;700;900&family=Montserrat:wght@700;800&display=swap" rel="stylesheet">
<style>
  :root{
    --stage:#2b2b2d;
    --card:#1b1b1c;
    --ink:#ffffff;
    --ink-soft:#cfcfd4;
    --violet:#a65ce6;
    --violet-deep:#8a3fd0;
    --lilac:#d9a6ff;
    --ice:#c7d3ff;
    --band-ink:#1a1a1c;
  }
  *{box-sizing:border-box;margin:0;padding:0}
  html,body{width:1200px;height:875px;overflow:hidden;background:var(--stage)}
  .stage{position:relative;width:1200px;height:875px}
  .card{position:absolute;left:300px;width:600px;height:343px;border-radius:22px;background:var(--card);overflow:hidden;font-family:'Lato',sans-serif}
  .card--front{top:70px}
  .card--back{top:462px}

  .brand{display:flex;align-items:center;gap:14px;font-family:'Montserrat',sans-serif;font-weight:800;color:var(--ink);letter-spacing:.02em;line-height:1}
  .brand__dot{border-radius:50%;background:var(--violet);flex:none}
  .card--front .brand{position:absolute;left:0;right:0;top:118px;justify-content:center;font-size:58px}
  .card--front .brand__dot{width:46px;height:46px}
  .sectors{position:absolute;left:0;right:0;top:222px;text-align:center;font-weight:900;font-size:19px;letter-spacing:.2em;color:var(--violet)}

  .wave{position:absolute;inset:0;width:600px;height:343px}
  .card--back .brand{position:absolute;left:36px;top:48px;font-size:36px;gap:10px}
  .card--back .brand__dot{width:28px;height:28px}
  .person{position:absolute;left:36px;top:104px;width:272px}
  .person__name{font-family:'Montserrat',sans-serif;font-weight:800;font-size:27px;color:var(--violet);letter-spacing:.02em;white-space:nowrap}
  .person__role{text-align:right;font-size:14px;color:var(--ink-soft);margin-top:2px}
  .divider{position:absolute;left:322px;top:40px;width:1px;height:98px;background:var(--violet)}
  .contacts{position:absolute;left:338px;top:38px;list-style:none}
  .contacts li{display:flex;align-items:center;gap:9px;font-size:12.5px;color:var(--ink-soft);height:27px;white-space:nowrap}
  .contacts svg{width:13px;height:13px;flex:none;fill:var(--violet)}
  .contacts li:first-child{font-size:15px}

  .offer{position:absolute;left:0;right:0;top:240px;text-align:center;color:var(--band-ink)}
  .offer__title{font-weight:900;font-size:19px;letter-spacing:.02em;text-transform:uppercase}
  .services{display:flex;justify-content:center;align-items:center;gap:7px;font-weight:700;font-size:13px;margin-top:7px}
  .tick{width:13px;height:13px;flex:none}
</style>
</head>
<body>
<div class="stage">

  <section class="card card--front" aria-label="Card front">
    <div class="brand"><span class="brand__dot"></span>FROSTLINE</div>
    <p class="sectors">RESIDENTIAL COMMERCIAL DIARY</p>
  </section>

  <section class="card card--back" aria-label="Card back">
    <svg class="wave" viewBox="0 0 600 343" aria-hidden="true">
      <defs>
        <linearGradient id="bandFill" x1="0" y1="0" x2="1" y2="1">
          <stop offset="0" stop-color="#c7d3ff"/>
          <stop offset=".45" stop-color="#d48cff"/>
          <stop offset="1" stop-color="#a65ce6"/>
        </linearGradient>
      </defs>
      <path d="M0,205 C170,195 330,212 430,168 C495,140 545,134 600,132 L600,343 L0,343 Z" fill="#8a3fd0"/>
      <path d="M0,219 C170,209 335,226 436,182 C500,154 548,148 600,146 L600,343 L0,343 Z" fill="#1b1b1c"/>
      <path d="M0,225 C170,215 338,232 440,188 C503,160 550,154 600,152 L600,343 L0,343 Z" fill="url(#bandFill)"/>
    </svg>

    <div class="brand"><span class="brand__dot"></span>FROSTLINE</div>
    <div class="person">
      <p class="person__name">WARREN KOSTIG</p>
      <p class="person__role">Director</p>
    </div>
    <span class="divider"></span>
    <ul class="contacts">
      <li><svg viewBox="0 0 24 24"><path d="M6.6 10.8a15.1 15.1 0 0 0 6.6 6.6l2.2-2.2a1 1 0 0 1 1-.25 11.4 11.4 0 0 0 3.6.57 1 1 0 0 1 1 1V20a1 1 0 0 1-1 1A17 17 0 0 1 3 4a1 1 0 0 1 1-1h3.5a1 1 0 0 1 1 1c0 1.25.2 2.45.57 3.57a1 1 0 0 1-.25 1z"/></svg>0491 357 208</li>
      <li><svg viewBox="0 0 24 24"><path d="M2 5h20v14H2zM3.5 6.5 12 13l8.5-6.5z"/></svg>info@frostlinerefrigeration.com.au</li>
      <li><svg viewBox="0 0 24 24"><path d="M12 2a10 10 0 1 0 0 20 10 10 0 0 0 0-20zm6.9 9h-3a15 15 0 0 0-1.3-5.6A8 8 0 0 1 18.9 11zM12 4.1c.9 1.3 1.7 3.6 1.9 6.9h-3.8c.2-3.3 1-5.6 1.9-6.9zM9.4 5.4A15 15 0 0 0 8.1 11h-3a8 8 0 0 1 4.3-5.6zM5.1 13h3a15 15 0 0 0 1.3 5.6A8 8 0 0 1 5.1 13zm6.9 6.9c-.9-1.3-1.7-3.6-1.9-6.9h3.8c-.2 3.3-1 5.6-1.9 6.9zm2.6-1.3a15 15 0 0 0 1.3-5.6h3a8 8 0 0 1-4.3 5.6z"/></svg>frostlinerefrigeration.com.au</li>
    </ul>

    <div class="offer">
      <p class="offer__title">We offer 24/7 emergency service</p>
      <p class="services">Air Conditioning
        <svg class="tick" viewBox="0 0 16 16"><circle cx="8" cy="8" r="8" fill="#1a1a1c"/><path d="M4.5 8.3l2.3 2.2 4.7-4.8" stroke="#d48cff" stroke-width="1.8" fill="none"/></svg>
        Refrigeration
        <svg class="tick" viewBox="0 0 16 16"><circle cx="8" cy="8" r="8" fill="#1a1a1c"/><path d="M4.5 8.3l2.3 2.2 4.7-4.8" stroke="#d48cff" stroke-width="1.8" fill="none"/></svg>
        Cool / Freezer Rooms
        <svg class="tick" viewBox="0 0 16 16"><circle cx="8" cy="8" r="8" fill="#1a1a1c"/><path d="M4.5 8.3l2.3 2.2 4.7-4.8" stroke="#d48cff" stroke-width="1.8" fill="none"/></svg>
        Ice Machines</p>
      <p class="services">Installation
        <svg class="tick" viewBox="0 0 16 16"><circle cx="8" cy="8" r="8" fill="#1a1a1c"/><path d="M4.5 8.3l2.3 2.2 4.7-4.8" stroke="#d48cff" stroke-width="1.8" fill="none"/></svg>
        Service &amp; Repair
        <svg class="tick" viewBox="0 0 16 16"><circle cx="8" cy="8" r="8" fill="#1a1a1c"/><path d="M4.5 8.3l2.3 2.2 4.7-4.8" stroke="#d48cff" stroke-width="1.8" fill="none"/></svg>
        Preventative Maintenance</p>
    </div>
  </section>

</div>
</body>
</html>
```